Diesel Fitting/Mechanical Company Needs a new Business Card

We would like a new business card that showcases our logo and business information.

Industry/Entity Type

Business

Contact Information for Business Card

314 Wendale Street
PO Box 7581 KESTON VALE QLD 4871
Phone: 49312787 Fax: 49312688 Mobile: 0438915276 ABN: 63 519 087 342

Requirements
Must have
• The following email addresses:
• admin@tkservicing.com.au , sales@tkservicing.com.au , accounts@tkservicing.com.au , parts@tkservicing.com.au , office@tkservicing.com.au
• Also need to have the website: www.tkservicing.com.au

```html
<!DOCTYPE html>
<html lang="en">
<head>
<meta charset="utf-8">
<title>TK Servicing – Business Card</title>
<link href="https://fonts.googleapis.com/css2?family=Open+Sans:wght@400;600;700&display=swap" rel="stylesheet">
<style>
  :root {
    --backdrop: #141517;
    --paper: #fbfbfb;
    --orange: #f47a24;
    --red: #e8232c;
    --yellow: #f7d51d;
    --ink: #1d1d1d;
    --grey: #5b5b5b;
    --white: #ffffff;
  }
  html, body {
    margin: 0;
    width: 1200px;
    height: 1000px;
    overflow: hidden;
    background: var(--backdrop);
    font-family: "Open Sans", Arial, sans-serif;
  }
  .canvas { position: relative; width: 1200px; height: 1000px; }
  .card {
    position: absolute;
    width: 500px;
    height: 286px;
    background: var(--paper);
    overflow: hidden;
    box-shadow: 0 10px 30px rgba(0,0,0,.5);
  }
  /* Back side */
  .card-back { left: 60px; top: 357px; }
  .back-panel {
    position: absolute; right: 0; top: 0;
    width: 290px; height: 100%;
    background: var(--orange);
  }
  .mail-badge {
    position: absolute; left: 198px; top: 86px;
    width: 28px; height: 28px;
  }
  .email-list {
    position: absolute; right: 28px; top: 80px;
    margin: 0; padding: 0; list-style: none;
    text-align: right; color: var(--white);
    font-size: 14px; font-weight: 600; line-height: 26px;
  }
  /* Front side */
  .card-front { left: 640px; top: 357px; }
  .brand {
    position: absolute; left: 34px; top: 62px;
    display: flex; align-items: center; gap: 10px;
  }
  .brand-dot { width: 22px; height: 22px; border-radius: 50%; background: var(--orange); }
  .brand-name { font-size: 26px; font-weight: 700; color: var(--orange); }
  .abn {
    position: absolute; left: 36px; top: 124px;
    font-size: 14px; color: var(--ink);
  }
  .abn strong { font-weight: 700; }
  .abn-bar {
    position: absolute; left: 32px; top: 146px;
    width: 170px; height: 9px; background: var(--yellow);
  }
  .person {
    position: absolute; left: 290px; top: 56px;
    padding-left: 14px; border-left: 6px solid var(--yellow);
    line-height: 1.1;
  }
  .person-name { font-size: 17px; font-weight: 700; color: var(--orange); letter-spacing: .5px; }
  .person-role { font-size: 15px; color: var(--grey); }
  .contacts {
    position: absolute; left: 292px; top: 108px;
    margin: 0; padding: 0; list-style: none;
    font-size: 13.5px; color: var(--ink); line-height: 19px;
  }
  .contacts li { display: flex; align-items: center; gap: 10px; }
  .contacts svg { width: 11px; height: 12px; }
  .address {
    position: absolute; left: 292px; top: 172px;
    font-size: 12.5px; line-height: 16px; color: var(--ink);
  }
  .footer-band { position: absolute; left: 0; bottom: 0; width: 500px; height: 72px; }
  .website {
    position: absolute; left: 50px; bottom: 20px;
    font-size: 15px; font-weight: 700; color: var(--white);
  }
</style>
</head>
<body>
<main class="canvas">
  <section class="card card-back" aria-label="Card back">
    <div class="back-panel"></div>
    <svg class="mail-badge" viewBox="0 0 28 28" aria-hidden="true">
      <circle cx="14" cy="14" r="13" fill="var(--orange)" stroke="#fff" stroke-width="2"/>
      <rect x="7.5" y="9.5" width="13" height="9" fill="#fff"/>
      <path d="M7.5 9.5 L14 15 L20.5 9.5" fill="none" stroke="var(--orange)" stroke-width="1.4"/>
    </svg>
    <ul class="email-list">
      <li>admin@tkservicing.com.au</li>
      <li>sales@tkservicing.com.au</li>
      <li>accounts@tkservicing.com.au</li>
      <li>parts@tkservicing.com.au</li>
      <li>office@tkservicing.com.au</li>
    </ul>
  </section>

  <section class="card card-front" aria-label="Card front">
    <div class="brand">
      <span class="brand-dot"></span>
      <span class="brand-name">TK Servicing</span>
    </div>
    <div class="abn"><strong>ABN</strong>: 63 519 087 342</div>
    <div class="abn-bar"></div>

    <div class="person">
      <div class="person-name">DANIEL HARPER</div>
      <div class="person-role">Manager</div>
    </div>
    <ul class="contacts">
      <li><svg viewBox="0 0 12 12" aria-hidden="true"><path d="M3 1 L5 3.5 L4 5 Q5.5 7.5 7 8 L8.5 7 L11 9 L9.5 11 Q4 10.5 1 3 Z" fill="var(--red)"/></svg>49 31 2787</li>
      <li><svg viewBox="0 0 12 12" aria-hidden="true"><rect x="3" y="1" width="6" height="3" fill="var(--red)"/><rect x="1" y="4" width="10" height="6" rx="1" fill="var(--red)"/><rect x="3" y="7" width="6" height="4" fill="#fff" stroke="var(--red)"/></svg>49 31 2688</li>
      <li><svg viewBox="0 0 12 12" aria-hidden="true"><rect x="3" y="0.5" width="6" height="11" rx="1" fill="none" stroke="var(--red)" stroke-width="1.4"/></svg>04 38 91 5276</li>
    </ul>
    <div class="address">
      314 Wendale Street<br>
      PO Box 7581<br>
      KESTON VALE QLD 4871
    </div>

    <svg class="footer-band" viewBox="0 0 500 72" aria-hidden="true">
      <path d="M0 42 H12 Q14 14 44 12 H266 Q294 14 300 42 H500 V72 H0 Z" fill="var(--red)"/>
    </svg>
    <div class="website">www.tkservicing.com.au</div>
  </section>
</main>
</body>
</html>
```